Building company buisness cards

We are looking for a sharp modern new look for our business cards.We are a New Zealand based company that specialises in house and land packages.We have attached a photo of the current logo and would like to see if it can be improved somehow if needed.We are open to any colours but we have chosen Black and White at this stage. Feel free to change the font and make the logo smarter looking.Play with the colours and see what looks best.We want a card that looks so good know one will want to throw it away!

Target Market(s)

Building profesonals, home buyers

Industry/Entity Type

Building

Contact Information for Business Card

Derek Haskins
0274930268
derekh@stonerange.co.nz

Font styles to use
Serif
Sans Serif

Colors

Designer to choose colors to be used in the design.

Requirements
Must have
• Just the logo on one side and details on the other
• Clean simple looking card
Nice to have
• Round corners and detail like raised or spot UV
• Something that stands out
Should not have
• To title needed, Director etc

```html
<!DOCTYPE html>
<html lang="en">
<head>
<meta charset="utf-8">
<title>Stonerange Business Card</title>
<link rel="stylesheet" href="https://fonts.googleapis.com/css2?family=Jost:wght@400;500&display=swap">
<style>
  :root {
    --backdrop: #e4e4e4;
    --card-front: #ffffff;
    --card-back: #0b0c10;
    --name-navy: #1f2a5a;
    --detail-grey: #555555;
    --brand-silver: #c9c9c9;
  }
  html, body {
    margin: 0;
    padding: 0;
    width: 1125px;
    height: 1200px;
    overflow: hidden;
    background: var(--backdrop);
  }
  .canvas {
    position: relative;
    width: 1125px;
    height: 1200px;
    font-family: "Jost", "Helvetica Neue", Arial, sans-serif;
  }
  .card {
    position: absolute;
    left: 156px;
    width: 826px;
    height: 471px;
    border-radius: 26px;
    display: flex;
    flex-direction: column;
    align-items: center;
    justify-content: center;
    box-sizing: border-box;
  }
  .card--details {
    top: 106px;
    background: var(--card-front);
  }
  .card--brand {
    top: 639px;
    background: var(--card-back);
  }
  .holder-name {
    margin: -16px 0 0;
    font-size: 46px;
    font-weight: 400;
    letter-spacing: 0.5px;
    color: var(--name-navy);
    text-transform: uppercase;
    line-height: 1;
  }
  .contact-line {
    margin: 14px 0 0;
    font-size: 19px;
    font-weight: 400;
    color: var(--detail-grey);
    letter-spacing: 0.2px;
  }
  .contact-line .divider {
    margin: 0 4px 0 8px;
  }
  .brand-name {
    margin-top: -8px;
    font-size: 80px;
    font-weight: 400;
    color: var(--brand-silver);
    line-height: 1;
    letter-spacing: 0.5px;
  }
</style>
</head>
<body>
<main class="canvas">
  <section class="card card--details" aria-label="Contact side">
    <h1 class="holder-name">Derek Haskins</h1>
    <p class="contact-line">0274930268<span class="divider">|</span>derekh@stonerange.co.nz<span class="divider">|</span>www.stonerange.co.nz</p>
  </section>
  <section class="card card--brand" aria-label="Brand side">
    <span class="brand-name">Stonerange</span>
  </section>
</main>
</body>
</html>
```